Tallgrove Vale Management

I need a professional website. My current website is tallgrovevalemanagement.com and I hate it. It was created with some AI tool very quickly because I needed a site up and running with no advanced notice. I’m open to all designs .. I trust you, the professionals will deliver the results I’m anxiously awaiting! :)

```html
<!DOCTYPE html>
<html lang="en">
<head>
<meta charset="utf-8">
<title>Tallgrove Vale Management — Property Management</title>
<link href="https://fonts.googleapis.com/css2?family=Playfair+Display:ital,wght@0,500;0,600;1,500;1,600&family=Inter:wght@400;500;600&display=swap" rel="stylesheet">
<style>
:root{
  --navy:#111822;
  --char:#1e1d1b;
  --card:#1a2029;
  --card-warm:#252422;
  --line:#2c333d;
  --gold:#c9a15a;
  --gold-deep:#b48a45;
  --white:#f4f1ea;
  --muted:#9a9ea5;
  --body:#c2c4c8;
}
*{box-sizing:border-box;margin:0;padding:0}
html,body{width:1200px;height:3555px;overflow:hidden;background:var(--navy);color:var(--white);font-family:"Inter",Arial,sans-serif}
section,header,footer{position:relative;overflow:hidden}
.wrap{width:758px;margin:0 auto;position:relative}
.eyebrow{display:flex;align-items:center;gap:8px;color:var(--gold);font-size:9px;font-weight:600;letter-spacing:2.2px;text-transform:uppercase}
.eyebrow::before{content:"";width:18px;height:1px;background:var(--gold)}
.h2{font-family:"Playfair Display",Georgia,serif;font-weight:600;font-size:31px;line-height:34px;color:var(--white)}
.lead{font-size:11px;line-height:19px;color:var(--body)}
.btn{display:inline-flex;align-items:center;gap:8px;height:33px;padding:0 20px;border-radius:20px;font-size:10px;font-weight:600;white-space:nowrap}
.btn-gold{background:var(--gold);color:#1b1a17}
.btn-ghost{border:1px solid #5b5e62;color:var(--white)}

/* hero */
.hero{height:618px;background:linear-gradient(180deg,#2b3230 0%,#1f2a24 30%,#1a2220 60%,#151b1f 100%)}
.hero-photo{position:absolute;inset:0;background:radial-gradient(ellipse at 70% 20%,rgba(120,130,120,.25),transparent 55%),radial-gradient(ellipse at 30% 70%,rgba(40,60,40,.35),transparent 60%)}
.nav{position:absolute;top:14px;left:0;right:0}
.nav .wrap{display:flex;align-items:center;height:28px}
.brand{display:flex;align-items:center;gap:7px;font-size:10px;font-weight:600;color:var(--white);width:120px}
.brand i{width:12px;height:12px;border-radius:50%;background:var(--gold)}
.nav ul{display:flex;gap:25px;list-style:none;font-size:9.5px;font-weight:500;margin-left:18px}
.nav .btn{margin-left:auto;height:26px;padding:0 14px;font-size:9px}
.hero-copy{position:absolute;left:380px;top:169px;width:460px}
.hero h1{font-family:"Playfair Display",Georgia,serif;font-weight:600;font-size:48px;line-height:55px;margin-top:12px;white-space:nowrap}
.hero h1 em{color:var(--gold);font-style:italic}
.tagline{font-family:"Playfair Display",Georgia,serif;font-style:italic;color:var(--gold);font-size:16px;margin-top:12px}
.hero .lead{margin-top:12px;width:370px}
.hero .actions{display:flex;gap:12px;margin-top:26px}

/* about */
.about{height:634px;background:var(--navy)}
.about-inner{padding-top:86px}
.about-top{display:flex;justify-content:space-between}
.about-text{width:320px}
.about-text .h2{margin-top:12px}
.about-text .lead{margin-top:20px}
.photo{border-radius:12px;box-shadow:0 20px 40px rgba(0,0,0,.45)}
.photo-bath{width:339px;height:193px;margin-top:14px;background:linear-gradient(110deg,#5b4a39 0%,#a88f72 45%,#d7c4a6 70%,#8f7558 100%)}
.grid4{display:grid;grid-template-columns:repeat(4,1fr);gap:16px}
.feature{background:var(--card);border:1px solid var(--line);border-radius:10px;height:167px;padding:22px 17px}
.ico{width:28px;height:28px;border-radius:7px;background:#2b2f35;display:flex;align-items:center;justify-content:center}
.ico svg{width:13px;height:13px;stroke:var(--gold);fill:none;stroke-width:1.6}
.feature h3,.service h3{font-size:11.5px;font-weight:600;margin-top:17px}
.feature p,.service p{font-size:9px;line-height:15.5px;color:var(--muted);margin-top:8px}
.about .grid4{margin-top:78px}

/* services */
.services{background:var(--char);height:499px;padding-top:93px}
.services .h2{margin-top:14px}
.services .lead{margin-top:10px;width:410px}
.services .grid4{margin-top:42px}
.service{background:var(--card-warm);border:1px solid #34322f;border-radius:10px;height:182px;padding:24px 18px;position:relative}
.service .ico{width:33px;height:33px;border:1px solid var(--gold-deep);background:transparent}
.service .num{position:absolute;top:18px;right:18px;font-family:"Playfair Display",Georgia,serif;font-size:9px;color:var(--muted)}

/* why */
.why{height:528px;padding-top:83px;background:var(--navy)}
.why .wrap{display:flex;justify-content:space-between}
.why-text{width:320px;padding-top:25px}
.why .h2{margin-top:12px}
.why .lead{margin-top:18px}
.checks{list-style:none;margin-top:18px}
.checks li{display:flex;align-items:center;gap:10px;font-size:10px;height:32.5px;color:var(--white)}
.checks svg{width:18px;height:18px}
.photo-city{width:353px;height:361px;background:linear-gradient(180deg,#c9dbe9 0%,#b9cfde 18%,#7e8f7d 28%,#4f6b3e 50%,#3f5a33 75%,#5b6b4e 100%)}

/* process */
.process{background:var(--char);height:486px;padding-top:92px}
.process .h2{margin-top:14px;width:430px}
.process .lead{margin-top:14px;width:430px}
.steps{display:grid;grid-template-columns:repeat(4,1fr);gap:16px;margin-top:52px;position:relative}
.steps::before{content:"";position:absolute;left:0;right:0;top:20px;height:1px;background:var(--gold-deep)}
.step-dot{width:42px;height:42px;border-radius:50%;background:#2a2822;border:1px solid #4a4130;position:relative;display:flex;align-items:center;justify-content:center;font-family:"Playfair Display",Georgia,serif;color:var(--gold);font-size:12px}
.step h3{font-size:11.5px;font-weight:600;margin-top:22px}
.step p{font-size:9px;line-height:15.5px;color:var(--muted);margin-top:8px;width:170px}

/* cta */
.cta{height:538px;padding-top:86px;background:var(--navy)}
.cta-box{height:365px;border:1px solid var(--line);border-radius:16px;background:linear-gradient(135deg,#23231f 0%,#1b2027 55%,#1d232b 100%);text-align:center;padding-top:80px}
.cta .eyebrow{justify-content:center}
.cta h2{font-family:"Playfair Display",Georgia,serif;font-weight:600;font-size:36px;line-height:42px;margin-top:14px}
.cta .lead{width:330px;margin:16px auto 0;line-height:14px;font-size:10.5px}
.cta .btn{margin-top:22px;height:32px}

/* footer */
.footer{height:252px;padding-top:58px;background:var(--navy)}
.foot-cols{display:grid;grid-template-columns:234px 178px 179px 1fr}
.foot-about p{font-size:9px;line-height:16px;color:var(--muted);margin-top:10px;width:180px}
.foot-col h4{font-size:9px;font-weight:600;letter-spacing:1.8px;color:var(--gold);text-transform:uppercase}
.foot-col ul{list-style:none;margin-top:10px}
.foot-col li{font-size:9.5px;color:var(--body);line-height:20px}
.foot-bottom{display:flex;justify-content:space-between;border-top:1px solid var(--line);margin-top:40px;padding-top:14px;font-size:8px;color:var(--muted)}
</style>
</head>
<body>

<header class="hero">
  <div class="hero-photo" role="img" aria-label="Aerial view of a tree-lined residential neighborhood with a city skyline in the distance, darkened overlay"></div>
  <nav class="nav">
    <div class="wrap">
      <div class="brand"><i></i>Tallgrove Vale</div>
      <ul><li>Home</li><li>About Us</li><li>Services</li><li>Our Approach</li><li>Investors</li><li>Contact</li></ul>
      <span class="btn btn-gold">Schedule Consultation →</span>
    </div>
  </nav>
  <div class="hero-copy">
    <div class="eyebrow">Cleveland · Akron — Property Management</div>
    <h1>A True Partner, Not<br>Just <em>a Vendor.</em></h1>
    <p class="tagline">Expertise Rooted in Asset Preservation</p>
    <p class="lead">Rigorously tested frameworks and data-driven methodologies safeguard property value while elevating the tenant experience — built for owners who expect more than management.</p>
    <div class="actions"><span class="btn btn-gold">Get Started →</span><span class="btn btn-ghost">Learn More</span></div>
  </div>
</header>

<section class="about">
  <div class="wrap about-inner">
    <div class="about-top">
      <div class="about-text">
        <div class="eyebrow">About Tallgrove Vale Management</div>
        <h2 class="h2">Property Management Built Around Performance</h2>
        <p class="lead">Our organization delivers comprehensive property management solutions that optimize asset performance and tenant satisfaction. By integrating advanced analytics with proven operational frameworks, our specialists ensure each property achieves sustained value appreciation across every market cycle.</p>
      </div>
      <div class="photo photo-bath" role="img" aria-label="Modern bathroom vanity with stone basin, brass faucet and round mirror"></div>
    </div>
    <div class="grid4">
      <div class="feature"><div class="ico"><svg viewBox="0 0 16 16"><path d="M8 1.5 13.5 3.5v4c0 3.5-2.5 6-5.5 7-3-1-5.5-3.5-5.5-7v-4Z"/></svg></div><h3>Asset Protection</h3><p>Proactive maintenance and disciplined oversight that preserves capital and reduces risk exposure.</p></div>
      <div class="feature"><div class="ico"><svg viewBox="0 0 16 16"><circle cx="6" cy="5" r="2.5"/><path d="M1.5 14c0-3 2-4.5 4.5-4.5s4.5 1.5 4.5 4.5M11 3a2.5 2.5 0 0 1 0 5M12.5 10c1.5.5 2.5 2 2.5 4"/></svg></div><h3>Tenant Experience</h3><p>Responsive communication and streamlined service that keeps residents satisfied and retained.</p></div>
      <div class="feature"><div class="ico"><svg viewBox="0 0 16 16"><path d="M2 2v12h12M4.5 10l3-3.5 2.5 2L14 4"/></svg></div><h3>Data Driven Management</h3><p>Portfolio decisions informed by real performance metrics, not assumptions or guesswork.</p></div>
      <div class="feature"><div class="ico"><svg viewBox="0 0 16 16"><path d="M4 13V10M8 13V7M12 13V3"/></svg></div><h3>Long Term Growth</h3><p>Strategic planning focused on sustained value appreciation across market conditions.</p></div>
    </div>
  </div>
</section>

<section class="services">
  <div class="wrap">
    <div class="eyebrow">What We Do</div>
    <h2 class="h2">Services Designed for Owners</h2>
    <p class="lead">A full-scope operating partner — from day-to-day property oversight to long-range portfolio strategy.</p>
    <div class="grid4">
      <div class="service"><span class="num">01</span><div class="ico"><svg viewBox="0 0 16 16"><path d="M2 7.5 8 2.5l6 5M3.5 6.5V14h9V6.5M6.5 14v-4h3v4"/></svg></div><h3>Property Management</h3><p>Full operational oversight — leasing, maintenance, inspections, and day-to-day execution.</p></div>
      <div class="service"><span class="num">02</span><div class="ico"><svg viewBox="0 0 16 16"><path d="M8 1.5 13.5 3.5v4c0 3.5-2.5 6-5.5 7-3-1-5.5-3.5-5.5-7v-4Z"/></svg></div><h3>Asset Preservation</h3><p>Preventative programs and reserve planning that protect long-term property value.</p></div>
      <div class="service"><span class="num">03</span><div class="ico"><svg viewBox="0 0 16 16"><circle cx="6.5" cy="5" r="2.5"/><path d="M2 14c0-3 2-4.5 4.5-4.5S11 11 11 14M11.5 5.5h3M13 4v3"/></svg></div><h3>Tenant Relations</h3><p>Consistent communication and dependable service that reduces turnover and vacancy.</p></div>
      <div class="service"><span class="num">04</span><div class="ico"><svg viewBox="0 0 16 16"><path d="M2 2v12h12M5 11V8M8 11V6M11 11V9"/></svg></div><h3>Investor Support</h3><p>Transparent reporting and strategic counsel aligned with each owner's objectives.</p></div>
    </div>
  </div>
</section>

<section class="why">
  <div class="wrap">
    <div class="why-text">
      <div class="eyebrow">Why Owners Choose Us</div>
      <h2 class="h2">Disciplined Systems, Clear Communication</h2>
      <p class="lead">Decades of collective expertise inform a proven operating model — one built to demonstrate resilience for owners across diverse market conditions.</p>
      <ul class="checks">
        <li><svg viewBox="0 0 18 18"><circle cx="9" cy="9" r="8.5" fill="#2a2d30" stroke="#4a4130"/><path d="M5.5 9.2 8 11.5l4.5-5" fill="none" stroke="#c9a15a" stroke-width="1.4"/></svg>Professional Systems</li>
        <li><svg viewBox="0 0 18 18"><circle cx="9" cy="9" r="8.5" fill="#2a2d30" stroke="#4a4130"/><path d="M5.5 9.2 8 11.5l4.5-5" fill="none" stroke="#c9a15a" stroke-width="1.4"/></svg>Data-Based Decisions</li>
        <li><svg viewBox="0 0 18 18"><circle cx="9" cy="9" r="8.5" fill="#2a2d30" stroke="#4a4130"/><path d="M5.5 9.2 8 11.5l4.5-5" fill="none" stroke="#c9a15a" stroke-width="1.4"/></svg>Reliable Communication</li>
        <li><svg viewBox="0 0 18 18"><circle cx="9" cy="9" r="8.5" fill="#2a2d30" stroke="#4a4130"/><path d="M5.5 9.2 8 11.5l4.5-5" fill="none" stroke="#c9a15a" stroke-width="1.4"/></svg>Investor-Focused Approach</li>
        <li><svg viewBox="0 0 18 18"><circle cx="9" cy="9" r="8.5" fill="#2a2d30" stroke="#4a4130"/><path d="M5.5 9.2 8 11.5l4.5-5" fill="none" stroke="#c9a15a" stroke-width="1.4"/></svg>Local Market Knowledge</li>
      </ul>
    </div>
    <div class="photo photo-city" role="img" aria-label="Aerial photo of a leafy residential neighborhood with a downtown skyline on the horizon, Cleveland and Akron region"></div>
  </div>
</section>

<section class="process">
  <div class="wrap">
    <div class="eyebrow">Our Process</div>
    <h2 class="h2">A Clear Path From Analysis to Growth</h2>
    <p class="lead">Every engagement follows the same disciplined sequence — so owners always know what comes next.</p>
    <div class="steps">
      <div class="step"><div class="step-dot">01</div><h3>Analyze Property</h3><p>A full assessment of condition, performance, and market position establishes the baseline.</p></div>
      <div class="step"><div class="step-dot">02</div><h3>Build Strategy</h3><p>A tailored management plan is designed around the owner's objectives and asset profile.</p></div>
      <div class="step"><div class="step-dot">03</div><h3>Optimize Operations</h3><p>Systems are implemented and refined to improve efficiency, occupancy, and tenant satisfaction.</p></div>
      <div class="step"><div class="step-dot">04</div><h3>Preserve &amp; Grow Value</h3><p>Ongoing oversight and reporting keep the asset protected and positioned for long-term growth.</p></div>
    </div>
  </div>
</section>

<section class="cta">
  <div class="wrap">
    <div class="cta-box">
      <div class="eyebrow">Start the Conversation</div>
      <h2>Ready to Protect Your Real<br>Estate Investment?</h2>
      <p class="lead">Submit an inquiry to connect with a dedicated advisor who will evaluate your objectives and implement a strategy tailored to your portfolio.</p>
      <span class="btn btn-gold">Start a Conversation →</span>
    </div>
  </div>
</section>

<footer class="footer">
  <div class="wrap">
    <div class="foot-cols">
      <div class="foot-about">
        <div class="brand"><i></i>Tallgrove Vale</div>
        <p>A true partner in property management — rooted in asset preservation, data-driven operations, and long-term tenant relationships across Cleveland &amp; Akron.</p>
      </div>
      <div class="foot-col"><h4>Navigate</h4><ul><li>Home</li><li>About Us</li><li>Services</li><li>Our Approach</li></ul></div>
      <div class="foot-col"><h4>Company</h4><ul><li>Investors</li><li>Contact</li><li>Our Process</li></ul></div>
      <div class="foot-col"><h4>Contact</h4><ul><li>Cleveland &amp; Akron, Ohio</li><li>info@tallgrovevalemanagement.com</li></ul></div>
    </div>
    <div class="foot-bottom"><span>© 2026 Tallgrove Vale Management LLC. All rights reserved.</span><span>Property Management · Cleveland &amp; Akron</span></div>
  </div>
</footer>

</body>
</html>
```